Fancy looking Inspection Postcard

Postcard needed for customers to inspect their product once it is delivered. We'll be giving them the steps for inspecting their product and to contact us if any issues arise. Would like to see something that sticks out but uses our company's colors. Would like to see creativity. Possibly utilizing the diamond steel background like we have in our logo.

Target Market(s)

Customers of our manufacturing shop

Industry/Entity Type

Manufacturing - metal wall art, custom products

Requirements
Must have
• our colors and logo
Nice to have
• get creative. i like creativity

```html
<!DOCTYPE html>
<html lang="en">
<head>
<meta charset="utf-8">
<title>Ridgeline Metalworks – Inspection Postcard</title>
<link href="https://fonts.googleapis.com/css2?family=Bebas+Neue&family=Poppins:wght@400;500;600;700&display=swap" rel="stylesheet">
<style>
  :root{
    --green:#6aa43a;
    --yellow:#fff200;
    --ink:#111111;
    --panel:#1e1e1e;
    --white:#ffffff;
    --page:#ffffff;
  }
  *{margin:0;padding:0;box-sizing:border-box}
  html,body{width:773px;height:1200px;overflow:hidden;background:var(--page);font-family:'Poppins',sans-serif}
  .postcard{position:absolute;left:49px;top:359px;width:675px;height:482px;background:var(--white);overflow:hidden;box-shadow:0 8px 22px rgba(0,0,0,.35)}
  .brand{position:absolute;left:30px;top:40px;width:88px;text-align:center}
  .brand-mark{width:34px;height:34px;background:var(--ink);margin:0 auto 6px}
  .brand-name{font-weight:700;font-size:10px;line-height:1.15;color:var(--green)}
  .headline{position:absolute;left:130px;top:34px}
  .headline .thanks{font-family:'Bebas Neue',sans-serif;font-size:46px;line-height:1;color:var(--green)}
  .headline .purchase{font-family:'Bebas Neue',sans-serif;font-size:37px;line-height:1;color:var(--ink);margin-top:2px}
  .headline .cta{font-weight:700;font-size:16.5px;line-height:1.2;color:var(--green)}
  .steps-panel{position:absolute;left:0;top:139px;width:470px;height:211px;background:var(--panel)}
  .steps-title{position:absolute;left:35px;top:11px;color:var(--white);font-weight:600;font-size:16px;line-height:20px;letter-spacing:.2px}
  .steps-title::after{content:"";position:absolute;left:0;top:24px;width:190px;height:1px;background:linear-gradient(90deg,#777,var(--green),transparent)}
  .step{position:absolute;width:180px;color:var(--white);line-height:1}
  .step-label{display:flex;align-items:center;width:max-content;height:19px;background:var(--yellow);color:var(--ink);font-weight:600;font-size:16px;line-height:19px;padding:0 6px}
  .step-label b{font-family:'Bebas Neue',sans-serif;font-weight:400;color:var(--green);font-size:22px;line-height:19px;margin-left:4px}
  .step-title{font-weight:600;font-size:10px;line-height:13px;margin-top:5px;text-transform:uppercase}
  .step ul{list-style:none;margin-top:1px}
  .step li{font-size:9px;line-height:13px;padding-left:13px;position:relative}
  .step li svg{position:absolute;left:0;top:2.5px}
  .rule-v{position:absolute;left:194px;top:42px;width:1px;height:160px;background:#555}
  .rule-h{position:absolute;top:116px;width:170px;height:1px;background:#666}
  .contact{position:absolute;left:35px;top:365px;font-size:10.5px;line-height:14px;color:var(--ink);white-space:nowrap}
  .contact b{font-weight:600}
  .contact .sep{color:var(--yellow);margin:0 7px;font-weight:600}
  .contact.second{left:188px;top:385px}
  .contact svg{vertical-align:-2px;margin:0 3px 0 6px}
  .footer{position:absolute;left:0;top:0;width:675px;height:482px}
  .good-job{position:absolute;left:37px;top:409px;color:var(--ink)}
  .good-job .small{font-weight:500;font-size:11.5px;line-height:13px}
  .good-job .big{font-weight:600;font-size:24px;line-height:26px}
  .review{position:absolute;left:202px;top:414px;color:var(--white);font-size:8.8px;line-height:12px;font-weight:500;white-space:nowrap}
  .review .lines{margin-top:3px;display:flex;gap:40px;font-size:10.5px;line-height:14px}
  .review svg{vertical-align:-1px;margin-right:4px}
  .shield{position:absolute;left:0;top:0;width:675px;height:482px}
</style>
</head>
<body>
<main class="postcard">
  <svg class="footer" viewBox="0 0 675 482" aria-hidden="true">
    <rect x="0" y="408" width="675" height="74" fill="#111"/>
    <path d="M0 388 H160 Q172 388 178 398 L229 482 H0 Z" fill="#fff200"/>
  </svg>

  <div class="brand">
    <div class="brand-mark"></div>
    <div class="brand-name">RIDGELINE METALWORKS</div>
  </div>

  <header class="headline">
    <div class="thanks">THANK YOU</div>
    <div class="purchase">FOR YOUR PURCHASE</div>
    <div class="cta">INSPECT YOUR PRODUCT NOW</div>
  </header>

  <section class="steps-panel">
    <h2 class="steps-title">FOLLOW THE BELOW STEPS</h2>
    <div class="rule-v"></div>
    <div class="rule-h" style="left:35px"></div>
    <div class="rule-h" style="left:228px"></div>

    <div class="step" style="left:35px;top:42px">
      <span class="step-label">STEP<b>1</b></span>
      <div class="step-title">Inspect general shape</div>
      <ul>
        <li><svg width="8" height="8" viewBox="0 0 8 8"><rect x=".5" y=".5" width="7" height="7" fill="none" stroke="#fff200"/><path d="M2 4l1.5 1.5L6.5 2" fill="none" stroke="#fff200"/></svg>Is it what you expected?</li>
        <li><svg width="8" height="8" viewBox="0 0 8 8"><rect x=".5" y=".5" width="7" height="7" fill="none" stroke="#fff200"/><path d="M2 4l1.5 1.5L6.5 2" fill="none" stroke="#fff200"/></svg>Is it bent, disoriented?</li>
      </ul>
    </div>

    <div class="step" style="left:35px;top:124px">
      <span class="step-label">STEP<b>2</b></span>
      <div class="step-title">Inspect the welds if<br>there are any</div>
      <ul>
        <li><svg width="8" height="8" viewBox="0 0 8 8"><rect x=".5" y=".5" width="7" height="7" fill="none" stroke="#fff200"/><path d="M2 4l1.5 1.5L6.5 2" fill="none" stroke="#fff200"/></svg>Do they look clean?</li>
        <li><svg width="8" height="8" viewBox="0 0 8 8"><rect x=".5" y=".5" width="7" height="7" fill="none" stroke="#fff200"/><path d="M2 4l1.5 1.5L6.5 2" fill="none" stroke="#fff200"/></svg>Are there any gaps?</li>
      </ul>
    </div>

    <div class="step" style="left:228px;top:42px;width:200px">
      <span class="step-label">STEP<b>3</b></span>
      <div class="step-title">Inspect the finish</div>
      <ul>
        <li><svg width="8" height="8" viewBox="0 0 8 8"><rect x=".5" y=".5" width="7" height="7" fill="none" stroke="#fff200"/><path d="M2 4l1.5 1.5L6.5 2" fill="none" stroke="#fff200"/></svg>Are there any areas not finished?</li>
        <li><svg width="8" height="8" viewBox="0 0 8 8"><rect x=".5" y=".5" width="7" height="7" fill="none" stroke="#fff200"/><path d="M2 4l1.5 1.5L6.5 2" fill="none" stroke="#fff200"/></svg>Are the colors what you expected?</li>
      </ul>
    </div>

    <div class="step" style="left:228px;top:124px;width:200px">
      <span class="step-label">STEP<b>4</b></span>
      <div class="step-title">Check for functionality</div>
      <ul>
        <li><svg width="8" height="8" viewBox="0 0 8 8"><rect x=".5" y=".5" width="7" height="7" fill="none" stroke="#fff200"/><path d="M2 4l1.5 1.5L6.5 2" fill="none" stroke="#fff200"/></svg>Does it work the way you want it to</li>
        <li><svg width="8" height="8" viewBox="0 0 8 8"><rect x=".5" y=".5" width="7" height="7" fill="none" stroke="#fff200"/><path d="M2 4l1.5 1.5L6.5 2" fill="none" stroke="#fff200"/></svg>Is it what you expected?</li>
      </ul>
    </div>
  </section>

  <p class="contact">Email us at
    <svg width="11" height="8" viewBox="0 0 11 8"><rect width="11" height="8" fill="#6aa43a"/><path d="M0 0l5.5 4.5L11 0" fill="none" stroke="#fff"/></svg><b>orders@ridgelinemetal.com</b><span class="sep">|</span>shoot us a text
    <svg width="10" height="10" viewBox="0 0 10 10"><path d="M2 1l2 2-1 1.5c.8 1.4 1.7 2.3 3 3L7.5 6l2 2-1.5 1.5C4.5 9 1 5.5.5 2.5z" fill="#6aa43a"/></svg><b>(555) 014-2290</b>
  </p>
  <p class="contact second">reach out via
    <svg width="11" height="11" viewBox="0 0 11 11"><circle cx="5.5" cy="5.5" r="5" fill="none" stroke="#6aa43a"/><ellipse cx="5.5" cy="5.5" rx="2" ry="5" fill="none" stroke="#6aa43a"/><path d="M.5 5.5h10" stroke="#6aa43a"/></svg><b>www.ridgelinemetal.com/contact</b>
  </p>

  <div class="good-job">
    <div class="small">DID WE DO A</div>
    <div class="big">GOOD JOB?</div>
  </div>

  <div class="review">
    If you think so, leave us a review on Reviewly? If not, Please let us know
    <div class="lines">
      <span><svg width="10" height="7" viewBox="0 0 10 7"><rect width="10" height="7" fill="#fff200"/><path d="M0 0l5 4 5-4" fill="none" stroke="#111"/></svg>info@ridgelinemetal.com</span>
      <span style="margin-left:30px"><svg width="9" height="9" viewBox="0 0 10 10"><path d="M2 1l2 2-1 1.5c.8 1.4 1.7 2.3 3 3L7.5 6l2 2-1.5 1.5C4.5 9 1 5.5.5 2.5z" fill="#fff200"/></svg>555-017-3361</span>
    </div>
  </div>

  <svg class="shield" viewBox="0 0 675 482">
    <defs>
      <linearGradient id="factory-tones" x1="0" y1="0" x2="1" y2="1">
        <stop offset="0" stop-color="#4d5f78"/>
        <stop offset=".45" stop-color="#8f98a6"/>
        <stop offset=".7" stop-color="#5b5f6a"/>
        <stop offset="1" stop-color="#a9b2bf"/>
      </linearGradient>
    </defs>
    <path d="M417 38 C500 46 562 36 595 34 C628 44 655 48 676 52 L676 388 C648 412 620 436 595 457 C518 422 468 382 442 322 C422 262 417 150 417 38 Z" fill="#fff200" stroke="#111" stroke-width="3"/>
    <g role="img" aria-label="Photo: smiling worker in a yellow hard hat and overalls giving a thumbs up in a metal fabrication shop">
      <path d="M432 54 C500 60 558 54 586 52 C620 60 650 64 676 68 L676 370 C648 394 620 416 595 437 C526 405 478 370 456 316 C438 262 432 160 432 54 Z" fill="url(#factory-tones)"/>
    </g>
  </svg>
</main>
</body>
</html>
```